Flyer für Kassensysteme
Zielgruppe
Kassensysteme - für diesen Flyer ist die Zielgruppe - Vereine - Unternehmen welche Vereinsfeste / Straßenfeste / Karnevalsitzungen oder Hausmessen bz. Messeverkäufe durchführen
Aufgabenstellung
optimal wäre DIN A5 einseitig welches auch so als Werbemail versendet werden kann. (unsere Internetpräsenz soll für diesen Firmenzweig von uns dann identisch angepasst werden) also ein schnell zu erfassender Flyer das es um Leih und Mietkassen für oben genannte Aktivitäten geht. kleiner Preis große Ersparnis Transparenz einfach zu bedienen

```html
<!DOCTYPE html>
<html lang="de">
<head>
<meta charset="utf-8">
<title>Leih- / Mietkassen Flyer</title>
<link rel="stylesheet" href="https://fonts.googleapis.com/css2?family=Montserrat:wght@400;500;600;700;800&display=swap">
<style>
  :root {
    --page-bg: #b4b4b4;
    --paper: #ffffff;
    --navy: #3f5770;
    --steel: #5d7d9c;
    --sky: #a9cde6;
    --mist: #94b3c8;
    --rule: #a8c8de;
    --purple: #6b2a6e;
    --ink: #2e2e2e;
    --grey-text: #4a4a4a;
  }
  * { box-sizing: border-box; margin: 0; padding: 0; }
  html, body { width: 1200px; height: 1200px; overflow: hidden; }
  body {
    background: var(--page-bg);
    font-family: "Montserrat", sans-serif;
    position: relative;
  }
  .flyer {
    position: absolute;
    left: 176px; top: 0;
    width: 848px; height: 1200px;
    background: var(--paper);
    overflow: hidden;
  }
  .hero { position: absolute; left: 0; top: 0; width: 848px; height: 570px; }

  .brand {
    position: absolute; left: 57px; top: 58px;
    display: flex; flex-direction: column; align-items: flex-start; gap: 12px;
  }
  .brand-square { width: 62px; height: 62px; background: var(--navy); }
  .brand-name {
    font-weight: 600; font-size: 20px; color: var(--navy);
    letter-spacing: 0.5px; line-height: 1; white-space: nowrap;
  }

  .headline {
    position: absolute; left: 0; width: 100%; top: 585px;
    text-align: center; font-weight: 800; font-size: 58px;
    color: var(--purple); letter-spacing: 0.5px; line-height: 1;
  }
  .subhead {
    position: absolute; left: 0; width: 100%; top: 660px;
    text-align: center; font-weight: 700; font-size: 26px;
    color: var(--grey-text); line-height: 38px;
  }
  .intro {
    position: absolute; left: 53px; top: 797px; width: 300px;
    font-weight: 700; font-size: 15px; line-height: 22px; color: var(--ink);
  }
  .divider {
    position: absolute; left: 369px; top: 758px;
    width: 3px; height: 198px; background: var(--rule);
  }
  .details {
    position: absolute; left: 388px; top: 755px; width: 408px;
    font-weight: 400; font-size: 15px; line-height: 22px; color: var(--ink);
    text-align: justify; letter-spacing: 0.4px;
  }
  .club-note {
    position: absolute; left: 0; width: 100%; top: 988px;
    text-align: center; font-weight: 700; font-size: 19.5px; color: var(--purple);
  }

  .footer { position: absolute; left: 0; top: 1032px; width: 848px; height: 168px; }
  .more-info {
    position: absolute; left: 54px; top: 1064px;
    font-weight: 700; font-size: 34px; color: var(--sky); letter-spacing: 0.5px;
  }
  .phone {
    position: absolute; left: 50px; top: 1116px;
    display: flex; align-items: center; gap: 20px;
  }
  .phone-number { font-weight: 700; font-size: 30px; color: #ffffff; letter-spacing: 0.3px; }
  .web {
    position: absolute; left: 417px; top: 1129px;
    font-weight: 700; font-size: 16px; color: var(--navy);
  }
</style>
</head>
<body>
  <main class="flyer">
    <svg class="hero" viewBox="0 0 848 570" xmlns="http://www.w3.org/2000/svg">
      <defs>
        <linearGradient id="festBlue" x1="0" y1="0" x2="1" y2="1">
          <stop offset="0" stop-color="#7f9fbd"/>
          <stop offset="1" stop-color="#4d6b8c"/>
        </linearGradient>
        <linearGradient id="grillBlue" x1="0" y1="0" x2="1" y2="1">
          <stop offset="0" stop-color="#7f9fbf"/>
          <stop offset="1" stop-color="#a8c2d8"/>
        </linearGradient>
        <linearGradient id="registerTone" x1="0" y1="0" x2="0" y2="1">
          <stop offset="0" stop-color="#4a4d52"/>
          <stop offset="0.6" stop-color="#8c9096"/>
          <stop offset="1" stop-color="#2f3236"/>
        </linearGradient>
      </defs>
      <polygon points="401,0 848,0 848,440 340,440 340,196 360,100" fill="var(--steel)"/>
      <rect x="428" y="0" width="420" height="440" fill="url(#grillBlue)" role="img" aria-label="Foto: Würstchen auf einem Grill am Festimbiss"/>
      <rect x="0" y="196" width="314" height="311" fill="url(#festBlue)" role="img" aria-label="Foto: Besucherin an einem Stand auf einem Vereinsfest"/>
      <path d="M212 372 L305 372 L305 120 Q305 96 330 96 L620 96 Q645 96 645 120 L645 360 L848 360 L848 564 L300 564 L300 545 L212 545 Z" fill="url(#registerTone)" role="img" aria-label="Produktfoto: Norvia Kassensystem mit Touch-Display, Tastatur und Bondrucker"/>
    </svg>

    <div class="brand">
      <span class="brand-square"></span>
      <span class="brand-name">KVL Kassensysteme</span>
    </div>

    <h1 class="headline">LEIH- / MIETKASSEN</h1>
    <p class="subhead">Sie planen bzw. veranstalten ein Vereinsfest eine<br>Hausmesse oder einen Sonderverkauf?</p>

    <p class="intro">Sparen Sie Zeit und Nerven mit der transparenten Abrechnung über eine unserer Mietkassen - kinderleicht zu bedienen und mit allen Funktionen eines modernen Kassensystems ausgestattet.</p>
    <span class="divider"></span>
    <p class="details">Unsere Mietkassen sind mit einem großen LCD-Display ausgesprochen benutzerfreundlich. Auch Aushilfen ohne jegliche Vorkenntnisse können an dem innovativen Kassensystem von Norvia schnell und fehlerfrei bedienen. Mit großer Tastatur für bis zu 75 verschiedene Artikel garantiert Ihnen eine hohe Flexibilität und Transparenz gewährleistet. Das alles zu einem äußerst attraktiven, budgetfreundlichen Preis.</p>

    <p class="club-note">Für Vereine bieten wir unsere Leihkassen mit einer Miet-TSE an.</p>

    <svg class="footer" viewBox="0 0 848 168" xmlns="http://www.w3.org/2000/svg">
      <rect x="0" y="0" width="848" height="6" fill="var(--mist)"/>
      <rect x="0" y="6" width="848" height="162" fill="var(--navy)"/>
      <path d="M345 148 C372 148 372 72 440 72 L848 72 L848 168 L0 168 L0 148 Z" fill="var(--mist)"/>
    </svg>
    <div class="more-info">MORE INFO</div>
    <div class="phone">
      <svg width="46" height="46" viewBox="0 0 46 46" xmlns="http://www.w3.org/2000/svg" aria-hidden="true">
        <circle cx="23" cy="23" r="23" fill="var(--sky)"/>
        <path d="M15.5 12.5c1-.9 2.4-.8 3.2.2l2.4 3c.7.9.6 2.1-.2 2.9l-1.5 1.4c1 2.4 2.9 4.6 5.4 5.9l1.5-1.4c.8-.8 2.1-.8 2.9-.1l3 2.5c1 .8 1.1 2.3.1 3.2l-1.6 1.6c-1.2 1.2-3 1.6-4.6 1-6.4-2.4-11-7.3-12.8-13.4-.5-1.6 0-3.3 1.2-4.4z" fill="var(--navy)"/>
      </svg>
      <span class="phone-number">[0761] 55302-0</span>
    </div>
    <div class="web">https://www.kvlkassen.de/leih-mietkassen/</div>
  </main>
</body>
</html>
```